Strategy and Technology Consulting - Our Story and Values Page

Interior Page design – Our History and Our Values

Our homepage has been designed and we are looking for a design for one of the interior pages. This interior page tells the story of Our History and Our Values

Because the homepage has been designed, we would like this interior page to reflect the design of the homepage without being a mirror image of the homepage.

This site will be implemented in WordPress using the Elementor framework.

Font: Poppins medium and Poppins dark
Illustrations: Our homepage illustrations were designed by “Welmo 1974” on Pixaborne. Compatible original or stock illustrations are welcome. Stock photography is also welcome. Welmo is also available through Welmo Trastek on Folivane

Uploaded Files
• Homepage design – this is the design we will use for our homepage. Contest entries should reflect this basic style but should be distinctly different from the homepage.
• Our History and Our Values – Wireframe – the basic layout of the page we are looking for.
• Our History and Our Values – Word document with the text supporting the wireframe.
• Color Palette – please use colors compatible with the palette attached.

Our Story - timeline
There is a timeline element in the wireframe. The wireframe displays this as a series of chevrons (arrows), but it does not need to be. Creativity in display of the timeline is appreciated.

Our Values
If you look at the Word document, you will see that there are a lot of words on the page. The winning design will present the information in a way that engages the user without overwhelming them with too much to read. For example, they may click on a value and see more information.

Target Market(s)

CIO's and Technology Executives

Number of Pages Required

1 page

Font styles to use
Sans Serif
Other font styles liked:
• Poppin

Requirements
Must have
• A timeline element, all of our values
Nice to have
• Clever timeline display

```html
<!DOCTYPE html>
<html lang="en">
<head>
<meta charset="utf-8">
<title>Veltrane – Our Story &amp; Our Values</title>
<link rel="stylesheet" href="https://fonts.googleapis.com/css2?family=Poppins:ital,wght@0,400;0,500;0,600;0,700;0,800;0,900;1,700;1,800&display=swap">
<style>
:root{
  --blue:#2a6497;
  --blue-deep:#1f5585;
  --blue-light:#3a78ad;
  --pale:#e6eef6;
  --yellow:#f0b91b;
  --ink:#2f3640;
  --text:#5a5f66;
  --card:#f1f1f1;
  --slate:#4b5a70;
  --slate-deep:#3f4c60;
  --white:#ffffff;
}
*{margin:0;padding:0;box-sizing:border-box}
html,body{width:1200px;height:4166px;overflow:hidden}
body{position:relative;background:var(--white);font-family:'Poppins',sans-serif;color:var(--text)}
.abs{position:absolute}

/* header */
.site-header{position:absolute;left:0;top:0;width:1200px;height:94px;border-bottom:1px solid #f0f0f0}
.brand{position:absolute;left:92px;top:22px;display:flex;align-items:center;gap:10px;font-family:'Poppins',sans-serif;font-weight:400;font-size:40px;color:#8d939b;letter-spacing:-0.5px}
.brand-dot{width:14px;height:14px;border-radius:50%;background:var(--blue)}
.nav{position:absolute;left:545px;top:37px;display:flex;gap:22px;align-items:center;font-size:12.5px;font-weight:600;color:#3b4654}
.nav span::after{content:"";display:inline-block;width:5px;height:5px;border-right:1.5px solid #3b4654;border-bottom:1.5px solid #3b4654;transform:rotate(45deg);margin-left:5px;position:relative;top:-3px}
.btn{display:inline-flex;align-items:center;justify-content:center;background:var(--yellow);color:var(--white);font-weight:700;font-size:12px;border-radius:30px;letter-spacing:.3px}
.header-cta{position:absolute;left:980px;top:27px;width:130px;height:38px}

/* story */
.section-title{font-family:'Poppins',sans-serif;font-weight:900;color:#3a4556;text-shadow:3px 4px 0 rgba(42,100,151,.12)}
.story-title{position:absolute;left:0;width:1200px;top:128px;text-align:center;font-size:60px;line-height:72px}
.story-intro{position:absolute;left:430px;width:340px;top:222px;text-align:center;font-size:14px;line-height:21px;color:#6a7079}
.step-num{position:absolute;font-weight:900;font-size:84px;color:#eef3f8;line-height:1}
.milestone{position:absolute;border-radius:50%;background:radial-gradient(circle at 35% 30%,var(--blue-light),var(--blue-deep));box-shadow:8px -6px 0 0 #fff,10px -4px 0 4px #e9f0f7;color:var(--white)}
.milestone-shadow{position:absolute;border-radius:50%;background:radial-gradient(ellipse,rgba(42,100,151,.35),rgba(42,100,151,0) 70%)}
.milestone h3{position:absolute;width:100%;text-align:center;font-style:italic;font-weight:800;font-size:21px}
.milestone ul{position:absolute;list-style:none;font-size:14.5px;line-height:17px}
.milestone li{position:relative;padding-left:19px;margin-bottom:9px}
.milestone li::before{content:"";position:absolute;left:0;top:3px;width:11px;height:11px;border-radius:50%;border:3px solid var(--yellow);background:transparent}
.milestone li.sub{padding-left:19px;margin-top:-6px;margin-bottom:4px}
.milestone li.sub::before{display:none}
.milestone b{font-weight:700}

/* values */
.values-title{position:absolute;left:76px;top:1268px;font-size:66px;color:var(--white);font-weight:900;line-height:80px}
.values-intro{position:absolute;left:76px;top:1352px;width:420px;font-size:14.5px;line-height:21px;color:var(--white)}
.value-card{position:absolute;left:76px;width:1051px;height:221px;background:var(--card);box-shadow:0 6px 14px rgba(0,0,0,.09)}
.value-media{position:absolute;top:0;width:318px;height:221px}
.value-media .frame{position:absolute;inset:0;background:#d9e3ee}
.value-media .photo{position:absolute;top:0;height:221px}
.media-left{left:0}
.media-left .frame{clip-path:polygon(0 0,86% 0,100% 50%,86% 100%,0 100%)}
.media-left .photo{left:0;width:306px;clip-path:polygon(0 0,86% 0,99% 50%,86% 100%,0 100%)}
.media-right{right:0}
.media-right .frame{clip-path:polygon(14% 0,100% 0,100% 100%,14% 100%,0 50%)}
.media-right .photo{right:0;width:306px;clip-path:polygon(14% 0,100% 0,100% 100%,14% 100%,1% 50%)}
.value-copy{position:absolute;top:22px}
.copy-right{left:354px;width:590px}
.copy-left{left:32px;width:640px}
.value-copy h3{font-weight:800;font-size:27px;color:#3a4556;line-height:40px;position:relative}
.value-copy h3::after{content:"";position:absolute;left:0;bottom:-4px;width:16px;height:4px;background:var(--yellow);border-radius:2px}
.value-copy p{margin-top:14px;font-size:14.2px;line-height:21.5px;color:#656a72}

/* newsletter */
.newsletter{position:absolute;left:137px;top:3457px;width:922px;height:205px;border-radius:103px;background:var(--yellow);box-shadow:0 10px 24px rgba(0,0,0,.12)}
.newsletter h2{position:absolute;left:81px;top:58px;font-weight:800;font-size:31px;color:var(--white)}
.newsletter p{position:absolute;left:81px;top:112px;width:420px;font-size:15px;line-height:19px;color:var(--white);font-weight:500}
.email-field{position:absolute;left:549px;top:81px;width:320px;height:44px;border-radius:22px;background:var(--white);display:flex;align-items:center;padding-left:24px;font-size:12px;color:#8b9097;gap:8px}
.email-send{position:absolute;right:4px;top:4px;width:36px;height:36px;border-radius:50%;background:#8fa0b3}

/* footer */
.footer-brand{position:absolute;left:121px;top:3846px;display:flex;align-items:center;gap:12px;font-size:62px;font-weight:400;color:#d8dde4;line-height:1}
.footer-brand .brand-dot{width:18px;height:18px;background:#8fb2d6}
.socials{position:absolute;left:176px;top:3920px;display:flex;gap:12px}
.socials span{width:40px;height:40px;border-radius:50%;background:#5d6c82;box-shadow:inset 0 0 0 2px #6e7d92}
.footer-cta{position:absolute;left:215px;top:3985px;width:130px;height:38px}
.footer-col{position:absolute;top:3820px;color:#e6eaf0}
.footer-col h4{font-weight:800;font-size:19px;color:var(--white);margin-bottom:14px}
.footer-col ul{list-style:none;font-size:12.5px;line-height:31.4px}
.footer-col li::before{content:"›";margin-right:7px;font-weight:700}
.contact-item{position:relative;padding-left:23px;font-size:12.5px;line-height:17px;margin-bottom:14px}
.contact-item svg{position:absolute;left:0;top:2px}
.copyright{position:absolute;left:0;top:4107px;width:1200px;height:59px;background:#3d495b;color:#e6eaf0;font-size:13px;font-weight:500;text-align:center;line-height:59px}
.chat-bubble{position:absolute;left:1134px;top:4082px;width:48px;height:48px;border-radius:50%;background:var(--yellow);display:flex;align-items:center;justify-content:center}
</style>
</head>
<body>

<header class="site-header">
  <div class="brand"><span class="brand-dot"></span>Veltrane</div>
  <nav class="nav">
    <svg width="16" height="14" viewBox="0 0 16 14"><path d="M8 0 0 7h2v7h4V9h4v5h4V7h2z" fill="#9aa3ad"/></svg>
    <span>ABOUT US</span><span>SERVICES</span><span>INSIGHTS</span><span>JOIN US</span>
  </nav>
  <a class="btn header-cta">CONTACT US</a>
</header>

<!-- Our Story -->
<h1 class="section-title story-title">Our Story</h1>
<p class="story-intro">Lorem ipsum dolor sit amet, consectetur adi piscing elit, sed do eiusmod tempor</p>

<svg class="abs" style="left:0;top:0" width="1200" height="1000" aria-hidden="true">
  <path d="M442 445 C560 520 640 625 815 619" fill="none" stroke="#2a6497" stroke-width="5" stroke-linecap="round" stroke-dasharray="0 14"/>
  <path d="M842 736 C790 815 710 862 604 858" fill="none" stroke="#2a6497" stroke-width="5" stroke-linecap="round" stroke-dasharray="0 14"/>
</svg>

<div class="step-num" style="left:113px;top:222px">1.</div>
<div class="step-num" style="left:808px;top:420px">2.</div>
<div class="step-num" style="left:243px;top:694px">3.</div>

<div class="milestone-shadow" style="left:150px;top:570px;width:270px;height:70px"></div>
<div class="milestone" style="left:123px;top:283px;width:308px;height:308px">
  <h3 style="top:56px">2018 – 2019</h3>
  <ul style="left:34px;top:102px;width:260px">
    <li>Growth Strategy Focus</li>
    <li>Consistent, Modest Growth</li>
    <li>Preliminary Focus on Technology</li>
    <li><b>Eureka!</b> Implementing strategy is hard</li>
  </ul>
</div>

<div class="milestone-shadow" style="left:848px;top:778px;width:270px;height:70px"></div>
<div class="milestone" style="left:821px;top:491px;width:308px;height:308px">
  <h3 style="top:76px">2020 – 2021</h3>
  <ul style="left:44px;top:122px;width:250px">
    <li>Pandemic Pauses Growth</li>
    <li><b>Rethinking:</b></li>
    <li class="sub">- The business model</li>
    <li class="sub">- The delivery model</li>
  </ul>
</div>

<div class="milestone-shadow" style="left:313px;top:1026px;width:270px;height:70px"></div>
<div class="milestone" style="left:286px;top:739px;width:308px;height:308px">
  <h3 style="top:76px">2022 &amp; onward</h3>
  <ul style="left:45px;top:122px;width:240px">
    <li>Leadership Team for Focus on Essential Areas</li>
    <li>Rapid Growth</li>
    <li>Customer Success</li>
  </ul>
</div>

<!-- Values band -->
<svg class="abs" style="left:0;top:0" width="1200" height="1500" aria-hidden="true">
  <path d="M0 1400 C60 1440 160 1470 260 1462 C420 1450 600 1410 800 1385 C960 1365 1100 1355 1200 1348 L1200 1360 C1000 1380 700 1420 500 1450 C330 1478 150 1478 0 1420Z" fill="#e6eef6"/>
  <path d="M0 1058 C120 1100 260 1160 400 1150 C600 1135 760 960 980 948 C1090 942 1160 985 1200 1020 L1200 1350 C1000 1370 760 1395 560 1430 C400 1458 260 1475 160 1458 C90 1446 40 1425 0 1398Z" fill="#2a6497"/>
</svg>
<h2 class="section-title values-title" style="text-shadow:none">Our Values</h2>
<p class="values-intro">Lorem ipsum dolor sit amet, consectetur adipisicing elit, sed do eiusmod tempor incididunt ut labore</p>

<article class="value-card" style="top:1499px">
  <div class="value-media media-left"><div class="frame"></div>
    <div class="photo" role="img" aria-label="Hands joining coloured puzzle pieces" style="background:linear-gradient(135deg,#e8dcc6,#c9b796 60%,#4d7fae)"></div></div>
  <div class="value-copy copy-right"><h3>The Value of Every Human. Regardless.</h3>
    <p>Each person's unique experiences and perspectives add vibrant hues to the tapestry of our shared existence.&nbsp; In a world where diversity paints the canvas of humanity, true beauty is found in recognizing the inherent and incalculable value of every human being.</p></div>
</article>

<article class="value-card" style="top:1759px">
  <div class="value-copy copy-left"><h3>Collaboration</h3>
    <p>Collaboration in work transforms individual endeavors into symphonies of collective achievement. Through collaboration, diverse talents converge, fostering a rich exchange of ideas that amplifies creativity, accelerates progress, and brings forth solutions beyond what a single mind could conceive.</p></div>
  <div class="value-media media-right"><div class="frame"></div>
    <div class="photo" role="img" aria-label="Team members joining hands in a circle seen from below" style="background:linear-gradient(135deg,#f4f6f8,#9aa7b6 45%,#2c3440)"></div></div>
</article>

<article class="value-card" style="top:2018px">
  <div class="value-media media-left"><div class="frame"></div>
    <div class="photo" role="img" aria-label="Sprinters at the start line on a running track" style="background:linear-gradient(180deg,#c8d5d9,#a7a49a 40%,#b24a3c 75%,#c7604f)"></div></div>
  <div class="value-copy copy-right"><h3>Passion</h3>
    <p>Passion infuses our work with energy, transforming routine tasks into opportunities for creativity and innovation. Fueled by passion, individuals become unstoppable forces, driven to overcome challenges and achieve remarkable outcomes that benefit them and inspire those around them.</p></div>
</article>

<article class="value-card" style="top:2278px">
  <div class="value-copy copy-left"><h3>Excellence</h3>
    <p>Excellence isn't a destination; it's a continuous journey of refinement and growth. Striving for excellence cultivates a culture of continuous improvement, fostering innovation, credibility, and a lasting impact that resonates far beyond the immediate task.</p></div>
  <div class="value-media media-right"><div class="frame"></div>
    <div class="photo" role="img" aria-label="Hikers walking a hill trail at sunset" style="background:linear-gradient(160deg,#e9b76a,#b98a45 40%,#6d6a35 70%,#3f4725)"></div></div>
</article>

<article class="value-card" style="top:2537px">
  <div class="value-media media-left"><div class="frame"></div>
    <div class="photo" role="img" aria-label="Climber scaling a rock face against blue sky" style="background:linear-gradient(100deg,#8a8376,#a39b8c 40%,#3e8fd6 70%,#2f7fc9)"></div></div>
  <div class="value-copy copy-right"><h3>Tenacity</h3>
    <p>Tenacity is the unwavering anchor that keeps us grounded amidst adversity, propelling us forward when faced with obstacles. The resilience to persist, adapt, and learn from setbacks leads to the mastery of skills and the fulfillment of ambitious goals.</p></div>
</article>

<article class="value-card" style="top:2797px">
  <div class="value-copy copy-left"><h3>Solution Mindset</h3>
    <p>A solution mindset is the compass that directs our focus from problems to possibilities. It empowers us to navigate challenges with a proactive mindset, igniting a journey of exploration and innovation that not only resolves issues but also paves the way for continuous growth and success.</p></div>
  <div class="value-media media-right"><div class="frame"></div>
    <div class="photo" role="img" aria-label="Hands holding a glowing light bulb in the dark" style="background:radial-gradient(circle at 55% 45%,#c9a36a,#4b3b2c 35%,#1d2226 75%)"></div></div>
</article>

<article class="value-card" style="top:3056px">
  <div class="value-media media-left"><div class="frame"></div>
    <div class="photo" role="img" aria-label="Colleagues gathered around a laptop in an office" style="background:linear-gradient(135deg,#d7d3cc,#8a7867 45%,#3d3530)"></div></div>
  <div class="value-copy copy-right"><h3>Generosity</h3>
    <p>Generosity creates a virtuous cycle of goodwill, fostering a sense of unity and shared purpose among colleagues. By freely sharing knowledge, support, and resources, we uplift those around us and contribute to a collaborative environment where collective achievements flourish.</p></div>
</article>

<!-- Footer -->
<svg class="abs" style="left:0;top:3400px" width="1200" height="766" aria-hidden="true">
  <path d="M0 80 C250 20 450 70 700 60 C900 52 1060 10 1200 40 L1200 766 L0 766Z" fill="#4b5a70"/>
  <path d="M260 255 C420 330 640 340 820 300 C930 276 1000 262 1080 270 C1000 300 900 340 780 350 C600 368 420 330 260 255Z" fill="#f3f5f8"/>
  <path d="M0 766 L0 400 C300 440 500 560 700 600 C900 640 1050 560 1200 520 L1200 766Z" fill="#46556b" opacity=".6"/>
</svg>

<section class="newsletter">
  <h2>Subscribe Our Newsletter</h2>
  <p>Subscribe our newsletter to receive the latest news and exclusive offers every week, No spam.</p>
  <div class="email-field">
    <svg width="14" height="10" viewBox="0 0 14 10"><rect width="14" height="10" rx="1" fill="#9aa3ad"/><path d="M0 1 7 6 14 1" stroke="#fff" fill="none"/></svg>
    Enter email address
    <span class="email-send"><svg width="36" height="36" viewBox="0 0 36 36"><path d="M11 18 25 11 21 26 18 20Z" fill="#fff"/></svg></span>
  </div>
</section>

<div class="footer-brand"><span class="brand-dot"></span>Veltrane</div>
<div class="socials"><span></span><span></span><span></span><span></span></div>
<a class="btn footer-cta">CONTACT US</a>

<div class="footer-col" style="left:490px"><h4>Quick links</h4>
  <ul><li>Home</li><li>About Us</li><li>Services</li><li>Insights</li><li>Join Us</li><li>Contact Us</li></ul></div>
<div class="footer-col" style="left:668px"><h4>Our Services</h4>
  <ul><li>Business Transformation</li><li>ERP Implementations</li><li>ERP Solutions</li><li>BI and Data</li><li>Building the Right Team...</li></ul></div>
<div class="footer-col" style="left:899px"><h4>Contact info</h4>
  <div class="contact-item"><svg width="13" height="10" viewBox="0 0 13 10"><rect width="13" height="10" rx="1" fill="#f0b91b"/><path d="M0 1 6.5 6 13 1" stroke="#4b5a70" fill="none"/></svg>Email:<br>hello@veltrane-mail.com</div>
  <div class="contact-item"><svg width="13" height="13" viewBox="0 0 13 13"><path d="M3 0 5 3 3.5 5C4.5 7 6 8.5 8 9.5L10 8l3 2-1.5 3C5.5 12.5.5 7.5 0 1.5Z" fill="#f0b91b"/></svg>Phone:<br>+44 120 555 0147</div>
  <div class="contact-item"><svg width="11" height="14" viewBox="0 0 11 14"><path d="M5.5 0A5.5 5.5 0 0 0 0 5.5C0 9.5 5.5 14 5.5 14S11 9.5 11 5.5A5.5 5.5 0 0 0 5.5 0Zm0 8A2.5 2.5 0 1 1 5.5 3a2.5 2.5 0 0 1 0 5Z" fill="#f0b91b"/></svg>Location:<br>Some address line goes<br>here city name</div>
</div>

<div class="copyright">© Veltrane Design 2023, All Rights Reserved</div>
<div class="chat-bubble"><svg width="24" height="22" viewBox="0 0 24 22"><path d="M12 1C5.9 1 1 5 1 10c0 2.6 1.3 4.9 3.4 6.6L3 21l5-2.4c1.2.3 2.6.5 4 .5 6.1 0 11-4 11-9S18.1 1 12 1Z" fill="#fff"/><circle cx="8" cy="10" r="1.4" fill="#f0b91b"/><circle cx="12" cy="10" r="1.4" fill="#f0b91b"/><circle cx="16" cy="10" r="1.4" fill="#f0b91b"/></svg></div>

</body>
</html>
```